Kestrel Calisthenics Gym Website

We need a website design for our gym.

Kestrel is the UAE's first calisthenics and parkour gym. The theme under which the gym revolves is that one does not require any machinery to workout as our bodies could be themselves the machinery. The gym is designed to be the more of a social hub rather than an "in-and-out" gym, where people come train, have fun, hang out and socialize for a few hours rather than just train for 60 minutes then leave. The gym is designed to be a big open space with lots of natural sunlight, natural wood and plants all over the place to create a natural and refreshing setting. We also use recycled material throughout the gym and recycle our waste as being green is part of our philosophy. We currently also have some of the world's top and most recognized calisthenics athletes working with us.

We would like our website to reflect all that as well as provide a simple, interactive and fun way for visitors to be able to get class and gym information, check out gym media and contact us for bookings.

Target Market(s)

Ages 15-35

Industry/Entity Type

Fitness

Coding

Coded - Design and coding required

Number of Pages Required

4 page

Font styles to use
Decorative

Colors
0792cd

Requirements
Must have
• Class descriptions
• Gym description
• Class schedules
• Trainer profiles
• Gym philosophy
• Contact Details
Nice to have
• A link to contact us directly for a free first trial class

```html
<!DOCTYPE html>
<html lang="en">
<head>
<meta charset="utf-8">
<title>Kestrel Calisthenics Gym</title>
<link href="https://fonts.googleapis.com/css2?family=Open+Sans:ital,wght@0,400;0,600;0,700;0,800;1,700;1,800&family=Roboto+Condensed:wght@400;700&display=swap" rel="stylesheet">
<style>
:root{
  --blue:#0792cd;
  --blue-dark:#0b5f8c;
  --blue-deep:#0a4a6e;
  --ink:#222;
  --grey:#666;
  --light:#f2f2f2;
  --row:#e3e3e3;
  --white:#fff;
  --orange:#f0a020;
}
*{margin:0;padding:0;box-sizing:border-box}
html,body{width:1200px;height:4813px;overflow:hidden}
body{position:relative;background:var(--white);font-family:"Open Sans",sans-serif;color:var(--ink)}
.abs{position:absolute}
.heading{font-family:"Open Sans",sans-serif;font-weight:800;font-style:italic;text-transform:uppercase;text-align:center;letter-spacing:.5px}

/* header */
.site-header{top:0;left:0;width:1200px;height:112px;background:var(--white)}
.brand{left:48px;top:30px;display:flex;align-items:center;gap:10px}
.brand-dot{width:14px;height:14px;background:var(--blue);border-radius:50%}
.brand-name{font-size:38px;font-weight:800;color:var(--ink)}
.brand-sub{left:74px;top:78px;font-size:13px;color:var(--grey)}
.main-nav{right:34px;top:46px;display:flex;gap:4px;font-family:"Roboto Condensed",sans-serif;font-size:16px;text-transform:uppercase}
.main-nav a{color:var(--ink);text-decoration:none;padding:6px 10px}
.main-nav a.active{border:1px solid var(--blue);color:var(--blue)}

/* hero */
.hero{top:112px;left:0;width:1200px;height:600px;background:linear-gradient(90deg,#6b4a2e 0%,#3c2c1f 40%,#1a1a1a 62%,#0d0d0d 100%)}
.hero-floor{top:470px;left:0;width:660px;height:130px;background:linear-gradient(180deg,#8a3325,#5e241c)}
.hero-copy{left:680px;top:100px;width:420px;color:var(--white);text-align:center}
.hero-copy h1{font-size:31px;font-weight:800;font-style:italic;line-height:1.2;text-transform:uppercase}
.hero-copy p{font-size:19px;margin-top:14px;line-height:1.35}
.hero-copy p strong{color:var(--blue)}
.signup{left:680px;top:290px;width:374px}
.signup .field{height:38px;background:#e9e9e9;border-radius:3px;margin-bottom:12px;padding:9px 14px;font-size:14px;color:#777}
.signup .btn{height:46px;background:var(--blue);color:var(--white);font-weight:800;font-size:20px;text-align:center;line-height:46px;margin-top:4px}

/* classes */
.classes{top:712px;left:0;width:1200px;height:517px}
.classes .heading{top:56px;width:100%;font-size:30px;color:var(--ink)}
.classes .heading span{color:var(--blue)}
.class-card{top:140px;width:300px;text-align:center}
.class-photo{width:162px;height:162px;margin:0 auto;border:3px solid var(--blue)}
.class-card h3{margin-top:42px;font-weight:400;font-size:21px;letter-spacing:1px}
.rule{width:90px;height:5px;background:var(--blue);margin:10px auto 14px}
.class-card p{font-size:14px;color:var(--grey);line-height:1.35}

/* schedules */
.schedules{top:1229px;left:0;width:1200px;height:462px;background:linear-gradient(180deg,#1c7aa8,#0e5c86)}
.schedules .heading{top:50px;width:100%;color:var(--white);font-size:30px}
.calendar{left:187px;top:156px;width:378px;height:252px;background:var(--white);padding:10px 16px}
.cal-head{display:flex;justify-content:space-between;align-items:center;color:var(--orange);font-weight:700;font-size:16px;height:30px;border-bottom:1px solid #ddd}
.cal-grid{display:grid;grid-template-columns:repeat(7,1fr);text-align:center;font-size:13px;row-gap:6px;margin-top:8px}
.cal-grid .dn{color:var(--orange);font-weight:700}
.cal-grid .b{color:var(--blue);font-weight:700}
.cal-grid span{height:26px;line-height:26px;margin:0 auto;width:26px}
.cal-grid .sel{background:var(--blue);color:var(--white);border-radius:50%}
.cal-grid .ring{border:1px solid #555;border-radius:50%}
.date-box{left:585px;top:162px;width:80px;background:var(--white);text-align:center;padding:6px 0}
.date-box .d{font-size:30px;font-weight:700;line-height:1}
.date-box .m{font-size:14px;font-weight:700;text-transform:uppercase}
.date-box .y{background:#333;color:var(--white);font-size:13px;margin-top:6px;padding:3px 0}
.event-panel{left:675px;top:158px;width:318px;height:180px;border:3px solid var(--white);background:linear-gradient(135deg,#d9d4cf,#9fb6c4)}
.view-all{left:748px;top:360px;width:172px;height:38px;border:2px solid var(--white);border-radius:20px;background:var(--blue);color:var(--white);font-style:italic;font-size:16px;display:flex;align-items:center;justify-content:center;gap:10px}

/* gym */
.gym{top:1691px;left:0;width:1200px;height:395px}
.gym .heading{top:52px;width:100%;color:var(--blue);font-size:30px}
.gym-text{top:130px;left:70px;width:1060px;text-align:center;font-size:14px;color:var(--grey);line-height:1.5}
.gym-text p+p{margin-top:14px}
.learn-more{left:452px;top:312px;width:296px;height:38px;background:var(--blue);color:var(--white);font-weight:700;font-size:16px;text-align:center;line-height:38px}

/* trainers */
.trainers{top:2086px;left:0;width:1200px;height:642px;background:linear-gradient(180deg,#176c97,#0e4f72)}
.trainers .heading{top:46px;width:100%;color:var(--white);font-size:30px}
.trainer{top:138px;width:248px;height:452px;border:3px solid var(--white);padding:16px 18px;text-align:center;color:var(--white)}
.trainer-photo{height:300px;background:linear-gradient(180deg,#b83a2a,#7a6a60)}
.trainer-photo.alt{background:linear-gradient(180deg,#8a8f96,#4f555c)}
.trainer h3{margin-top:34px;font-size:18px;font-weight:800;font-style:italic;text-transform:uppercase}
.trainer .rule{background:var(--white);width:100%;height:1px;margin:12px 0 16px}
.trainer p{font-size:14px;font-weight:600;text-transform:uppercase}

/* testimonials */
.testimonials{top:2728px;left:0;width:1200px;height:417px}
.testimonials .heading{top:50px;width:100%;color:var(--blue);font-size:30px}
.client{top:142px;display:flex;align-items:center;gap:16px}
.avatar{width:116px;height:116px;border-radius:50%;border:4px solid var(--blue);background:radial-gradient(circle,#e8d7c8,#a8b9c7)}
.client-name{font-style:italic;font-size:18px}
.quote-mark{top:290px}
.testimonial-text{top:298px;left:140px;width:920px;text-align:center;font-size:14px;color:var(--grey);line-height:1.45}

/* pricing */
.pricing{top:3145px;left:0;width:1200px;height:642px;background:linear-gradient(180deg,#1a86bd,#0b6fa4)}
.pricing .heading{top:50px;width:100%;color:var(--white);font-size:30px}
.plan{top:140px;width:250px;height:450px;background:var(--white);border:3px solid var(--white);text-align:center}
.price{margin-top:40px;font-size:44px;font-weight:800;color:var(--blue)}
.term{font-size:15px;font-weight:700;margin-top:6px;text-transform:uppercase}
.features{margin-top:34px;font-size:13px;font-weight:700}
.features div{height:38px;line-height:38px}
.features div:nth-child(odd){background:var(--row)}
.buy{width:210px;height:38px;margin:28px auto 0;background:var(--blue);color:var(--white);font-weight:800;font-size:20px;line-height:38px}

/* gallery */
.gallery{top:3787px;left:0;width:1200px;height:603px;display:grid;grid-template-columns:repeat(4,1fr);grid-template-rows:repeat(2,1fr);gap:2px;background:var(--white)}
.tile{background:linear-gradient(160deg,#c9c9c9,#6f6f6f)}
.tile.warm{background:linear-gradient(160deg,#7a5a3d,#3a2d25)}
.tile.cool{background:linear-gradient(160deg,#c2d4e2,#5d8aa8)}

/* contact */
.contact{top:4390px;left:0;width:1200px;height:391px}
.map{top:0;left:0;width:1200px;height:391px;background:linear-gradient(135deg,#e9e5dc,#d6dce0)}
.contact-band{top:0;left:0}
.contact .heading{top:52px;left:104px;text-align:left;color:var(--white);font-size:30px}
.contact-list{top:128px;left:104px;color:var(--white);font-size:15px;list-style:none}
.contact-list li{display:flex;align-items:flex-start;gap:18px;margin-bottom:18px}
.social{top:290px;left:140px;display:flex;gap:8px}
.social span{width:14px;height:14px;border-radius:50%;background:var(--white)}

.site-footer{top:4781px;left:0;width:1200px;height:32px;font-size:11px;color:var(--grey);text-align:center;line-height:32px}
</style>
</head>
<body>

<header class="site-header abs">
  <div class="brand abs"><span class="brand-dot"></span><span class="brand-name">kestrel.</span></div>
  <div class="brand-sub abs">calisthenics gym</div>
  <nav class="main-nav abs">
    <a class="active">Home</a><a>Classes</a><a>Schedule</a><a>Gym</a><a>Trainers</a><a>Testimonials</a><a>Pricing</a><a>Gallery</a><a>Contact</a>
  </nav>
</header>

<section class="hero abs" role="img" aria-label="Gym interior with a green plant wall, wooden panels and rows of dumbbells">
  <div class="hero-floor abs"></div>
  <div class="hero-copy abs">
    <h1>Welcome to Kestrel<br>Calisthenics Gym</h1>
    <p>We're so sure you'll fall in love with <strong>KESTREL</strong><br>that we'll let you try a FREE Class.</p>
  </div>
  <form class="signup abs">
    <div class="field">Enter Your Name</div>
    <div class="field">Enter a Valid Email Address</div>
    <div class="field">Enter Your Phone Number</div>
    <div class="btn">SUBSCRIBE NOW</div>
  </form>
</section>

<section class="classes abs">
  <h2 class="heading abs">Start <span>your class</span> today</h2>
  <div class="class-card abs" style="left:120px">
    <div class="class-photo" role="img" aria-label="Gymnastic rings hanging in the gym" style="background:linear-gradient(160deg,#5d6670,#1f2a33)"></div>
    <h3>CALISTHENICS</h3><div class="rule"></div>
    <p>Lorem ipsum dolor sit amet, consectetuer<br>adipiscing elit, sed diam nonummy<br>nibh euismod tincidunt ut...</p>
  </div>
  <div class="class-card abs" style="left:450px">
    <div class="class-photo" role="img" aria-label="Parkour climbing frame" style="background:linear-gradient(160deg,#a84a30,#3a4f6a)"></div>
    <h3>PARKOUR</h3><div class="rule"></div>
    <p>Lorem ipsum dolor sit amet, consectetuer<br>adipiscing elit, sed diam nonummy<br>nibh euismod tincidunt ut...</p>
  </div>
  <div class="class-card abs" style="left:780px">
    <div class="class-photo" role="img" aria-label="Athlete training in the gym" style="background:linear-gradient(160deg,#c8b7a6,#6b5a4f)"></div>
    <h3>GYM</h3><div class="rule"></div>
    <p>Lorem ipsum dolor sit amet, consectetuer<br>adipiscing elit, sed diam nonummy<br>nibh euismod tincidunt ut...</p>
  </div>
</section>

<section class="schedules abs" aria-label="Class schedules">
  <h2 class="heading abs">Class Schedules</h2>
  <div class="calendar abs">
    <div class="cal-head">
      <svg width="12" height="14" viewBox="0 0 12 14"><path d="M10 1 3 7l7 6" fill="none" stroke="currentColor" stroke-width="2.5"/></svg>
      <span>OCT 2015</span>
      <svg width="12" height="14" viewBox="0 0 12 14"><path d="M2 1l7 6-7 6" fill="none" stroke="currentColor" stroke-width="2.5"/></svg>
    </div>
    <div class="cal-grid">
      <span class="dn">S</span><span class="dn">M</span><span class="dn">T</span><span class="dn">W</span><span class="dn">T</span><span class="dn">F</span><span class="dn">S</span>
      <span>4</span><span class="b">5</span><span>6</span><span class="b">7</span><span>8</span><span>9</span><span>10</span>
      <span>11</span><span class="sel">12</span><span>13</span><span>14</span><span>15</span><span>16</span><span>17</span>
      <span>18</span><span>19</span><span>20</span><span>21</span><span>22</span><span>23</span><span class="ring">24</span>
      <span>25</span><span>26</span><span>27</span><span class="ring">28</span><span>29</span><span>30</span><span>31</span>
    </div>
  </div>
  <div class="date-box abs"><div class="d">12</div><div class="m">Oct</div><div class="y">2015</div></div>
  <div class="event-panel abs" role="img" aria-label="Group fitness class in session"></div>
  <div class="view-all abs">View all
    <svg width="40" height="14" viewBox="0 0 40 14"><path d="M0 7h36M30 1l7 6-7 6" fill="none" stroke="#fff" stroke-width="2"/></svg>
  </div>
</section>

<section class="gym abs">
  <h2 class="heading abs">Gym</h2>
  <div class="gym-text abs">
    <p>Kestrel is the UAE's first calisthenics and parkour gym. The theme under which the gym revolves is that one does not require any machinery to workout as our bodies could be themselves the machinery. The gym is designed to be the more of a social hub rather than an "in-and-out" gym, where people come train, have fun, hang out and socialize for a few hours rather than just train for 60 minutes then leave.</p>
    <p>The gym is designed to be a big open space with lots of natural sunlight, natural wood and plants all over the place to create a natural and refreshing setting. We also use recycled material throughout the gym and recycle our waste as being green is part of our philosophy. We currently also have some of the world's top and most recognized calisthenics athletes working with us.</p>
  </div>
  <div class="learn-more abs">LEARN MORE</div>
</section>

<section class="trainers abs">
  <h2 class="heading abs">The Trainers</h2>
  <div class="trainer abs" style="left:118px">
    <div class="trainer-photo" role="img" aria-label="Portrait of calisthenics trainer"></div>
    <h3>Darren Okafor</h3><div class="rule"></div><p>Calisthenics Trainer</p>
  </div>
  <div class="trainer abs" style="left:442px">
    <div class="trainer-photo alt" role="img" aria-label="Portrait of yoga coach"></div>
    <h3>Lena Marsh</h3><div class="rule"></div><p>Yoga Coach</p>
  </div>
  <div class="trainer abs" style="left:766px">
    <div class="trainer-photo" role="img" aria-label="Portrait of parkour trainer"></div>
    <h3>Tariq Bennett</h3><div class="rule"></div><p>Parkour Trainer</p>
  </div>
</section>

<section class="testimonials abs">
  <h2 class="heading abs">Client Testimonials</h2>
  <div class="client abs" style="left:96px"><div class="avatar" role="img" aria-label="Client portrait"></div><span class="client-name">Hannah Ellery</span></div>
  <div class="client abs" style="left:466px"><div class="avatar" role="img" aria-label="Client portrait"></div><span class="client-name">Hannah Ellery</span></div>
  <div class="client abs" style="left:836px"><div class="avatar" role="img" aria-label="Client portrait"></div><span class="client-name">Hannah Ellery</span></div>
  <svg class="quote-mark abs" style="left:92px" width="40" height="34" viewBox="0 0 40 34"><path d="M2 34V18C2 8 8 2 16 0v6c-5 2-7 6-7 10h7v18zM24 34V18c0-10 6-16 14-18v6c-5 2-7 6-7 10h7v18z" fill="#0792cd"/></svg>
  <p class="testimonial-text abs">Lorem ipsum dolor sit amet, consectetuer adipiscing elit, sed diam nonummy nibh euismod tincidunt ut laoreet dolore magna aliquam erat volu. Wisi enim ad minim veniam, quis nostrud exerci tation ullamcorper suscipit lobortis nisl ut aliquip ex ea commodo consequat. Duis autem vel dolor in hendrerit in vulputate velit esse molestie consequat, vel illum dolore eu feugiat nulla facilisis at vero eros et accumsan et iusto.</p>
  <svg class="quote-mark abs" style="left:1068px;top:326px" width="40" height="34" viewBox="0 0 40 34"><path d="M38 0v16c0 10-6 16-14 18v-6c5-2 7-6 7-10h-7V0zM16 0v16c0 10-6 16-14 18v-6c5-2 7-6 7-10H2V0z" fill="#0792cd"/></svg>
</section>

<section class="pricing abs">
  <h2 class="heading abs">Kestrel Pricing Package</h2>
  <div class="plan abs" style="left:160px">
    <div class="price">€ 129</div><div class="term">3 Month Contract</div>
    <div class="features"><div>Classes 2x/week</div><div>Open Gym Monday - Friday</div><div>Yoga Relax Classes</div><div>Personal Training Session</div><div>Olympic Weightlifting</div></div>
    <div class="buy">BUY NOW</div>
  </div>
  <div class="plan abs" style="left:475px">
    <div class="price">€ 149</div><div class="term">6 Month Contract</div>
    <div class="features"><div>Classes 2x/week</div><div>Open Gym Monday - Friday</div><div>Yoga Relax Classes</div><div>Personal Training Session</div><div>Olympic Weightlifting</div></div>
    <div class="buy">BUY NOW</div>
  </div>
  <div class="plan abs" style="left:786px">
    <div class="price">€ 199</div><div class="term">12 Month Contract</div>
    <div class="features"><div>Classes 2x/week</div><div>Open Gym Monday - Friday</div><div>Yoga Relax Classes</div><div>Personal Training Session</div><div>Olympic Weightlifting</div></div>
    <div class="buy">BUY NOW</div>
  </div>
</section>

<section class="gallery abs" aria-label="Gym gallery">
  <div class="tile warm" role="img" aria-label="Plant wall and dumbbell rack"></div>
  <div class="tile" role="img" aria-label="Open training floor"></div>
  <div class="tile cool" role="img" aria-label="Climbing rig structure"></div>
  <div class="tile cool" role="img" aria-label="Sunlit training hall with mats"></div>
  <div class="tile warm" role="img" aria-label="Gymnastic rings close-up"></div>
  <div class="tile" role="img" aria-label="Row of dumbbells"></div>
  <div class="tile" role="img" aria-label="Gym equipment area"></div>
  <div class="tile cool" role="img" aria-label="Pull-up frame outdoors"></div>
</section>

<section class="contact abs">
  <div class="map abs" role="img" aria-label="Street map showing the gym location"></div>
  <svg class="contact-band abs" width="1200" height="391" viewBox="0 0 1200 391"><polygon points="0,0 790,0 560,391 0,391" fill="#0792cd"/></svg>
  <h2 class="heading abs">Contact Information</h2>
  <ul class="contact-list abs">
    <li><svg width="18" height="22" viewBox="0 0 18 22"><path d="M9 0a8 8 0 0 0-8 8c0 6 8 14 8 14s8-8 8-14a8 8 0 0 0-8-8zm0 11a3 3 0 1 1 0-6 3 3 0 0 1 0 6z" fill="#fff"/></svg><span>48 HARBOUR WALK, SUITE#210<br>DUBAI, UAE 312</span></li>
    <li><svg width="18" height="18" viewBox="0 0 18 18"><path d="M4 1l3 4-2 2c1 2 3 4 5 5l2-2 4 3-2 3C7 16 2 11 1 3z" fill="#fff"/></svg><span>+971.555.0142</span></li>
    <li><svg width="18" height="14" viewBox="0 0 18 14"><rect width="18" height="14" fill="#fff"/><path d="M0 0l9 7 9-7" fill="none" stroke="#0792cd" stroke-width="1.5"/></svg><span>info@kestrel.com</span></li>
  </ul>
  <div class="social abs"><span></span><span></span><span></span><span></span><span></span></div>
</section>

<footer class="site-footer abs">© 2015 KESTREL CALISTHENICS GYM. ALL RIGHTS RESERVED.</footer>

</body>
</html>
```